VORNAK (PTY)LTD Website design

WEBSITE design based on our different divisions in our organization.
Our company specializes in the following.
Construction
Property development
Demolition
Mining
Transport
Manufacturing of concrete bricks and blocks
Lightweight concrete Readymix
I want a very modern website and look that fits in with our organization and the changing times of the world.
The website must be very professional and crisp and should appeal to both the younger generation and older generation of business leaders and.
The website must be very user friendly and easy to navigate, simple yet modern, professional and corporate.

```html
<!DOCTYPE html>
<html lang="en">
<head>
<meta charset="utf-8">
<title>VORNAK (PTY)LTD</title>
<link href="https://fonts.googleapis.com/css2?family=Open+Sans:wght@400;600;700&family=Raleway:wght@400;500;600;700&display=swap" rel="stylesheet">
<style>
:root{
  --blue:#1a8ed4;
  --blue-dark:#0f6fb0;
  --navy:#0d1b2a;
  --ink:#333;
  --muted:#8a8f95;
  --line:#e3e6ea;
  --paper:#ffffff;
  --soft:#f4f5f7;
}
*{box-sizing:border-box;margin:0;padding:0}
html,body{width:1200px;height:4260px;overflow:hidden}
body{position:relative;font-family:"Open Sans",Arial,sans-serif;color:var(--ink);background:var(--paper)}
.abs{position:absolute}
.photo{position:absolute;display:block}
h2.section-title{position:absolute;left:0;width:1200px;text-align:center;font-family:"Raleway",Arial,sans-serif;font-weight:600;font-size:34px;letter-spacing:1px;color:#222}

/* header / hero */
.hero{left:0;top:0;width:1200px;height:568px;background:linear-gradient(180deg,#3b4046 0%,#6b7178 35%,#9a9a94 62%,#4d4b45 100%)}
.brand{display:flex;align-items:center;gap:10px;white-space:nowrap}
.header-brand{left:28px;top:24px}
.brand-mark{width:22px;height:22px;background:var(--blue);flex:none}
.brand-name{font-family:"Raleway",Arial,sans-serif;font-weight:700;font-size:24px;color:#fff;letter-spacing:1px}
.main-nav{left:282px;top:34px;display:flex;gap:28px}
.main-nav a{font-family:"Raleway",Arial,sans-serif;font-size:12px;font-weight:700;color:#fff;text-decoration:none;letter-spacing:.5px;white-space:nowrap}
.social{left:1088px;top:34px;display:flex;gap:12px}
.social span{width:10px;height:10px;border-radius:50%;background:#fff;display:block}
.slider-dots{left:1166px;top:220px;display:flex;flex-direction:column;gap:10px}
.slider-dots span{width:6px;height:6px;border-radius:50%;background:#fff;opacity:.6}

/* services */
.services{left:0;top:568px;width:1200px;height:586px;background:linear-gradient(90deg,#ffffff 0%,#ffffff 60%,#eceae4 100%)}
.offer{left:170px;top:728px;width:202px;height:319px;border:2px dashed var(--blue);padding:100px 16px 0}
.offer h3{font-family:"Raleway",Arial,sans-serif;font-weight:600;color:var(--blue);font-size:20px;line-height:1.15}
.offer p{margin-top:12px;font-size:10.5px;line-height:1.5;color:var(--blue)}
.service-card .caption{position:absolute;left:0;font-family:"Raleway",Arial,sans-serif;font-size:15px;color:#222}
.view-all{left:905px;top:758px;width:131px;height:300px;border:2px solid var(--blue);border-right:none;background:#fff;padding:85px 0 0 38px}
.view-all p{font-family:"Raleway",Arial,sans-serif;font-size:18px;color:var(--blue);line-height:1.25}
.view-all .go{margin-top:10px;width:30px;height:30px;border-radius:50%;background:var(--blue);display:flex;align-items:center;justify-content:center}

/* about */
.about{left:0;top:1154px;width:1200px;height:586px;background:var(--soft)}
.quote{left:230px;top:1198px;width:740px;text-align:center;font-size:20px;line-height:1.45;color:#8a8f95}
.about-title{left:170px;top:1316px;font-family:"Raleway",Arial,sans-serif;font-weight:700;font-size:28px;color:#222}
.tabs{left:170px;top:1376px;width:400px;display:flex;gap:78px;border-bottom:1px solid var(--line);padding-bottom:8px}
.tabs span{font-size:9.5px;font-weight:600;color:#555;text-transform:uppercase}
.tabs span.on{color:var(--blue)}
.about-text{left:170px;top:1426px;width:400px;font-size:11.5px;line-height:1.8;color:#aaa}
.more{left:170px;top:1612px;font-size:10px;font-weight:700;color:#444;letter-spacing:.5px}

/* projects */
.filters{left:170px;top:1884px;display:flex;gap:22px}
.filters span{font-size:12px;color:#444;padding-bottom:4px;white-space:nowrap}
.filters span.on{border-bottom:2px solid var(--blue);color:#222;font-weight:600}

/* news */
.news{left:0;top:2610px;width:1200px;height:710px;background:#f5f5f5}
.card{background:#fff;box-shadow:0 2px 6px rgba(0,0,0,.08)}
.card .body{position:absolute;left:16px;right:16px;top:190px}
.card h4{font-family:"Raleway",Arial,sans-serif;font-size:15.5px;font-weight:500;color:#222}
.card p{margin-top:10px;font-size:10.5px;line-height:1.6;color:#999}
.card .meta{margin-top:12px;display:flex;gap:18px;font-size:10px;color:#777;align-items:center}
.card .meta i{display:inline-block;width:8px;height:8px;background:#777;margin-right:5px;vertical-align:middle}
.btn{position:absolute;left:16px;bottom:18px;width:96px;height:28px;border-radius:14px;background:var(--blue);color:#fff;font-size:11px;text-align:center;line-height:28px}
.dots{left:578px;top:3270px;display:flex;gap:6px}
.dots span{width:7px;height:7px;border-radius:50%;background:#bbb}
.dots span.on{background:var(--blue)}

/* locations */
.locations{left:0;top:3320px;width:1200px;height:568px;background:linear-gradient(180deg,#eef0f2,#e3e8ec)}
.loc{left:390px;width:420px;height:80px;background:#fff;box-shadow:0 2px 6px rgba(0,0,0,.06)}
.loc .thumb{position:absolute;left:0;top:0;width:100px;height:80px}
.loc h5{position:absolute;left:126px;top:22px;font-family:"Raleway",Arial,sans-serif;font-size:15px;font-weight:600;color:var(--blue)}
.loc p{position:absolute;left:126px;top:44px;font-size:11px;color:#888}

/* footer */
.footer{left:0;top:3888px;width:1200px;height:372px;background:var(--navy);color:#c7ced6}
.footer-brand{left:170px;top:3930px}
.f-col h6{font-size:11px;font-weight:700;color:#fff;letter-spacing:.5px;padding-bottom:8px;border-bottom:1px solid #2a3a4c;width:120px}
.f-col ul{list-style:none;margin-top:10px}
.f-col li{font-size:10.5px;line-height:22px;color:#b9c1cb}
.f-about{left:170px;top:3990px;width:190px;font-size:10.5px;line-height:1.6;color:#b9c1cb}
.f-social{left:170px;top:4110px;display:flex;gap:8px}
.f-social span{width:20px;height:20px;background:var(--blue-dark);display:block}
.post{display:flex;gap:10px;margin-top:12px}
.post .th{width:40px;height:32px;background:linear-gradient(135deg,#6e747a,#b59a52);flex:none}
.post b{display:block;font-size:10px;font-weight:400;color:#fff;text-decoration:underline;white-space:nowrap}
.post em{font-style:normal;font-size:9.5px;color:#8d97a3}
.copy{left:170px;top:4226px;font-size:10.5px;color:#8d97a3}
.copy-line{left:170px;top:4206px;width:860px;height:1px;background:#24344a}
</style>
</head>
<body>

<!-- header -->
<section class="abs hero" role="img" aria-label="Yellow excavator on a gravel heap under a cloudy sky"></section>
<div class="abs brand header-brand"><span class="brand-mark"></span><span class="brand-name">VORNAK</span></div>
<nav class="abs main-nav"><a>ABOUT</a><a>SERVICES</a><a>PROJECTS</a><a>NEWS &amp; MEDIA</a><a>CONTACT</a></nav>
<div class="abs social"><span></span><span></span><span></span></div>
<div class="abs slider-dots"><span></span><span></span><span></span></div>

<!-- services -->
<section class="abs services" role="img" aria-label="Faint close-up of a large truck tyre"></section>
<h2 class="section-title" style="top:640px">SERVICES</h2>
<div class="abs offer">
  <h3>WHAT WE<br>OFFER</h3>
  <p>We build, develop and move what matters. Our divisions cover the full chain from site works to supply, with crews you can rely on.</p>
</div>
<div class="abs service-card" style="left:408px;top:728px;width:220px;height:330px">
  <div class="photo" role="img" aria-label="Construction worker in safety gear on site" style="left:0;top:0;width:220px;height:310px;background:linear-gradient(160deg,#8fa3b8,#c58a3c 60%,#4d4a44)"></div>
  <span class="caption" style="top:314px">Construction</span>
</div>
<div class="abs service-card" style="left:642px;top:728px;width:216px;height:330px">
  <div class="photo" role="img" aria-label="Mining crew at an open rock face" style="left:0;top:0;width:216px;height:256px;background:linear-gradient(160deg,#7d8a94,#9a8f80 55%,#5a544c)"></div>
  <span class="caption" style="top:262px">Mining</span>
</div>
<div class="abs view-all">
  <p>View all<br>Services</p>
  <div class="go"><svg width="12" height="12" viewBox="0 0 12 12"><path d="M2 6h8M7 3l3 3-3 3" stroke="#fff" stroke-width="1.6" fill="none"/></svg></div>
</div>

<!-- about -->
<section class="abs about"></section>
<p class="abs quote">At vero eos et accusamus et iusto odio dignissimos ducimus qui blanditiis praesentium voluptatum deleniti atque corrupti quos dolores et quas molestias excepturi sint occaecati cupiditate non provident</p>
<h2 class="abs about-title">ABOUT US</h2>
<div class="abs tabs"><span class="on">Who we are</span><span>What we do</span><span>Our vision</span></div>
<p class="abs about-text">Vornak is a South African group working across construction, property development, demolition, mining and transport. We also make concrete bricks, blocks and lightweight readymix. Our teams plan, build and deliver projects of every size with care for safety, quality and time. We grow with our clients and the places we build.</p>
<span class="abs more">MORE ABOUT US &rsaquo;</span>
<div class="photo" role="img" aria-label="Modern brick office building at dusk" style="left:610px;top:1324px;width:420px;height:337px;background:linear-gradient(180deg,#5b7fa8 0%,#8aa0b8 40%,#4a3c34 100%)"></div>

<!-- projects -->
<h2 class="section-title" style="top:1822px">OUR PROJECTS</h2>
<div class="abs filters"><span class="on">All</span><span>Construction</span><span>Property development</span><span>Demolition</span><span>Mining</span><span>Transport</span><span>Concrete bricks and blocks</span><span>Concrete Readymix</span></div>
<div class="photo" role="img" aria-label="Workers on steel scaffolding" style="left:170px;top:1963px;width:420px;height:195px;background:linear-gradient(150deg,#6f8fb0,#b8743a 60%,#3e3a36)"></div>
<div class="photo" role="img" aria-label="Demolition excavator on a ruined building" style="left:610px;top:1963px;width:200px;height:195px;background:linear-gradient(160deg,#a7b4bf,#c9a244 55%,#6a6258)"></div>
<div class="photo" role="img" aria-label="Apartment block under construction" style="left:830px;top:1963px;width:200px;height:195px;background:linear-gradient(160deg,#7fa4c9,#8c8a86 60%,#4e4a46)"></div>
<div class="photo" role="img" aria-label="Concrete blocks on a production line" style="left:170px;top:2172px;width:420px;height:199px;background:linear-gradient(150deg,#8a8f94,#b04a3c 50%,#5a5a5a)"></div>
<div class="photo" role="img" aria-label="Haul truck in an open pit mine" style="left:610px;top:2172px;width:420px;height:199px;background:linear-gradient(160deg,#9c9588,#d0a43a 50%,#3e3a34)"></div>
<div class="photo" role="img" aria-label="Excavator at sunset" style="left:170px;top:2382px;width:200px;height:198px;background:linear-gradient(160deg,#e8b56a,#c77a2c 55%,#4a3a2a)"></div>
<div class="photo" role="img" aria-label="Worker guiding a concrete pour" style="left:390px;top:2382px;width:200px;height:198px;background:linear-gradient(160deg,#9aa6b0,#a79686 55%,#55504a)"></div>
<div class="photo" role="img" aria-label="Transport trucks on a highway at night" style="left:610px;top:2382px;width:420px;height:198px;background:linear-gradient(160deg,#2f4a66,#6f8fae 55%,#1c2a38)"></div>

<!-- news -->
<section class="abs news"></section>
<h2 class="section-title" style="top:2734px">NEWS</h2>
<article class="abs card" style="left:170px;top:2811px;width:274px;height:412px">
  <div class="photo" role="img" aria-label="Steel reinforcement bars on a building site" style="left:0;top:0;width:274px;height:178px;background:linear-gradient(150deg,#8fa0ae,#a65a3a 55%,#4c4a48)"></div>
  <div class="body"><h4>Sed ut perspiciatis unde omnis</h4><p>At vero eos et accusamus et iusto odio dignissimos ducimus qui blanditiis praesentium voluptatum deleniti atque corrupti quos.</p><div class="meta"><span><i></i>18.12.2018</span><span><i></i>Admin</span></div></div>
  <span class="btn">Read More</span>
</article>
<article class="abs card" style="left:462px;top:2811px;width:273px;height:412px">
  <div class="photo" role="img" aria-label="Workers pouring a concrete slab" style="left:0;top:0;width:273px;height:178px;background:linear-gradient(150deg,#9aa8b4,#b38a5a 55%,#5a544e)"></div>
  <div class="body"><h4>Ut enim ad minima veniam</h4><p>Et harum quidem rerum facilis est et expedita distinctio nam libero tempore cum soluta nobis est eligendi optio.</p><div class="meta"><span><i></i>18.12.2018</span><span><i></i>Admin</span></div></div>
  <span class="btn">Read More</span>
</article>
<article class="abs card" style="left:756px;top:2811px;width:274px;height:412px">
  <div class="photo" role="img" aria-label="Excavator moving earth" style="left:0;top:0;width:274px;height:178px;background:linear-gradient(150deg,#b7c3cc,#d6a83c 55%,#5e564a)"></div>
  <div class="body"><h4>Itaque earum rerum hic</h4><p>Nam libero tempore cum soluta nobis est eligendi optio cumque nihil impedit quo minus id quod maxime placeat.</p><div class="meta"><span><i></i>18.12.2018</span><span><i></i>Admin</span></div></div>
  <span class="btn">Read More</span>
</article>
<div class="abs dots"><span class="on"></span><span></span><span></span></div>

<!-- locations -->
<section class="abs locations" role="img" aria-label="Faint world map with location pins"></section>
<h2 class="section-title" style="top:3400px">OUR LOCATIONS</h2>
<div class="abs loc" style="top:3492px"><div class="thumb" role="img" aria-label="African savanna at sunset" style="background:linear-gradient(160deg,#e2a04a,#7a5a30)"></div><h5>AFRICA</h5><p>Project Area A</p></div>
<div class="abs loc" style="top:3632px"><div class="thumb" role="img" aria-label="Asian terraced hills" style="background:linear-gradient(160deg,#a7b86a,#4e6a3a)"></div><h5>ASIA</h5><p>Project Area B</p></div>
<div class="abs loc" style="top:3740px"><div class="thumb" role="img" aria-label="European old town skyline" style="background:linear-gradient(160deg,#c9a27a,#6a4a3a)"></div><h5>EUROPE</h5><p>Project Area C</p></div>

<!-- footer -->
<footer class="abs footer"></footer>
<div class="abs brand footer-brand"><span class="brand-mark"></span><span class="brand-name">VORNAK</span></div>
<p class="abs f-about">Vornak builds, develops, mines and moves. One group, many divisions, one standard of quality on every site we work.</p>
<div class="abs f-social"><span></span><span></span><span></span><span></span></div>
<div class="abs f-col" style="left:390px;top:3930px"><h6>COMPANY</h6><ul><li>About</li><li>Contact</li><li>Projects</li><li>Privacy Policy</li><li>Terms of use</li><li>News</li></ul></div>
<div class="abs f-col" style="left:532px;top:3930px"><h6>LATEST NEWS</h6>
  <div class="post"><div class="th" role="img" aria-label="News thumbnail"></div><div><b>New site opens in the Cape</b><em>18.12.2018 &nbsp; Admin</em></div></div>
  <div class="post"><div class="th" role="img" aria-label="News thumbnail"></div><div><b>Readymix plant upgraded</b><em>18.12.2018 &nbsp; Admin</em></div></div>
  <div class="post"><div class="th" role="img" aria-label="News thumbnail"></div><div><b>Fleet grows by ten trucks</b><em>18.12.2018 &nbsp; Admin</em></div></div>
</div>
<div class="abs f-col" style="left:827px;top:3930px"><h6>CONTACT</h6><ul><li>12 Harbour Road, Cape Town<br>8001 South Africa</li><li>+27 21 555 0142</li><li>info@vornak.co.za</li></ul></div>
<div class="abs copy-line"></div>
<p class="abs copy">&copy; Copyright 2018 VORNAK (PTY)LTD</p>

</body>
</html>
```